Single Page/Scrolling Design for Model Recruitment site

We need a design (and if you are capable, coding) for our company, Brimwell Parlour (LA as in Los Angeles). We like modern single page designs, hence the title for the project. We have already had a designer come up with a logo, which is attached. You're free to play around with the colors, although we want the site to have a feminine appeal to it.

The site is basically a recruitment project for girls who are interested in working as chat hosts for cam sites. We don't want anything cheesy that feels like a porn site. The inspiration for the logo (and the inspiration for the site) comes from the French and English salons of the late 18th century, where beautiful and intelligent women would gather to discuss a range of topics. We want the website to convey that this work is fun and exciting. Please keep these things in mind for the design.

As I mentioned, we like the modern look and feel of single page designs, especially because we don't have a ton of content. We just need an "About us" area, a "Work from Home" area, a "Work at The Brimwell Parlour" area, and "Contact Us" area which should have text boxes for entering email, subject, a message, etc.

The logo I mentioned is attached, as well as a very crude mockup of the layout of all the content I described.

Target Market(s)

Women age 18-35.

Industry/Entity Type

It Company

Font styles to use
Serif
Decorative
Script

Colors

Designer to choose colors to be used in the design.

Requirements
Should not have
• Images that are super sexual or even slightly pornographic. We want this to appeal to a broad range of women.

```html
<!DOCTYPE html>
<html lang="en">
<head>
<meta charset="utf-8">
<title>Brimwell Parlour</title>
<link rel="stylesheet" href="https://fonts.googleapis.com/css2?family=Arimo:wght@400;700&display=swap">
<style>
  :root {
    --pink: #db1a80;
    --pink-dark: #c90f6c;
    --gold: #d7a11f;
    --gold-dark: #d4960a;
    --cyan: #1fbcd5;
    --cyan-dark: #07afcd;
    --slate: #363c46;
    --slate-dark: #2c3038;
    --cream: #ece4d8;
    --cream-deep: #ddd2c2;
    --ink: #4a4a4a;
    --white: #ffffff;
    --ring: #c9c9c9;
  }
  * { box-sizing: border-box; margin: 0; padding: 0; }
  html, body { width: 1058px; height: 1200px; overflow: hidden; }
  body { position: relative; font-family: "Arimo", Arial, sans-serif; background: var(--white); }

  .site-nav { position: absolute; top: 0; left: 0; width: 1058px; height: 26px; background: var(--pink); display: flex; justify-content: center; }
  .site-nav a { display: block; height: 26px; line-height: 26px; font-size: 10.5px; color: var(--white); text-decoration: none; padding: 0 18px; letter-spacing: .2px; }
  .site-nav a.is-active { background: var(--white); color: #333; padding: 0 19px; }
  .site-nav ul { display: flex; list-style: none; margin-left: 40px; }

  .hero { position: absolute; top: 26px; left: 0; width: 1058px; height: 210px;
    background: linear-gradient(120deg, var(--cream) 0%, #f1ebe2 40%, var(--cream-deep) 75%, var(--cream) 100%); }
  .brand { position: absolute; left: 328px; top: 60px; width: 140px; display: flex; flex-direction: column; align-items: center; gap: 10px; }
  .brand-mark { width: 62px; height: 62px; border-radius: 50%; background: var(--pink); }
  .brand-name { font-size: 20px; font-weight: 700; color: var(--pink); text-align: center; line-height: 1.15; }
  .hero-intro { position: absolute; left: 482px; top: 58px; width: 262px; font-size: 14px; line-height: 23px; color: var(--ink); text-align: justify; }

  .band { position: absolute; left: 0; width: 1058px; }
  .band-title { position: relative; height: 30px; line-height: 30px; text-align: center; color: var(--white); font-weight: 700; font-size: 15px; }
  .band-title::after { content: ""; position: absolute; left: 519px; top: 30px; border: 10px solid transparent; border-top-width: 10px; border-bottom: 0; z-index: 2; }
  .band-body { position: relative; color: var(--white); font-size: 9.3px; line-height: 12.6px; }
  .band-body p { text-align: justify; }

  .about { top: 236px; }
  .about .band-title { background: var(--gold-dark); }
  .about .band-title::after { border-top-color: var(--gold-dark); }
  .about .band-body { background: var(--gold); height: 224px; padding: 24px 0 0 312px; }
  .about .band-body p { width: 438px; margin-bottom: 12px; }

  .train { top: 490px; }
  .train .band-title { background: var(--pink-dark); }
  .train .band-title::after { border-top-color: var(--pink-dark); }
  .train .band-body { background: var(--pink); height: 208px; padding: 18px 0 0 312px; }
  .train .band-body p { width: 282px; margin-bottom: 12px; }
  .train-visual { position: absolute; left: 602px; top: 38px; width: 142px; height: 126px; border-radius: 60px 60px 20px 20px; background: rgba(255,255,255,.9); }

  .remote { top: 728px; }
  .remote .band-title { background: var(--cyan-dark); }
  .remote .band-title::after { border-top-color: var(--cyan-dark); }
  .remote .band-body { background: var(--cyan); height: 208px; padding: 24px 0 0 312px; }
  .remote .band-body p { width: 438px; }
  .faq-links { position: absolute; top: 84px; left: 405px; display: flex; gap: 48px; }
  .faq-bubble { width: 100px; height: 100px; border-radius: 50%; background: var(--white); border: 7px solid var(--ring); display: flex; align-items: center; justify-content: center; text-align: center; color: #333; font-size: 14.5px; line-height: 17px; text-decoration: none; }

  .contact { top: 966px; }
  .contact .band-title { background: var(--slate-dark); }
  .contact .band-title::after { border-top-color: var(--slate-dark); }
  .contact .band-body { background: var(--slate); height: 204px; }
  .contact-icon { position: absolute; left: 328px; top: 14px; }
  .contact-form { position: absolute; left: 543px; top: 20px; width: 158px; }
  .contact-form label { display: block; font-size: 8.5px; color: var(--white); margin-bottom: 4px; }
  .contact-form input, .contact-form textarea { display: block; width: 158px; background: transparent; border: 1px solid #a9adb3; margin-bottom: 8px; font-family: inherit; }
  .contact-form input { height: 19px; }
  .contact-form textarea { height: 67px; resize: none; }
</style>
</head>
<body>
  <nav class="site-nav">
    <ul>
      <li><a class="is-active" href="#about">ABOUT US</a></li>
      <li><a href="#train">TRAIN @ THE BRIMWELL PARLOUR</a></li>
      <li><a href="#remote">WORK FROM HOME</a></li>
      <li><a href="#contact">CONTACT</a></li>
    </ul>
  </nav>

  <header class="hero">
    <div class="brand">
      <span class="brand-mark"></span>
      <span class="brand-name">Brimwell Parlour</span>
    </div>
    <p class="hero-intro">Welcome the Brimwell Parlour, a unique portal into the wordl of webcam modeling and chat hosting</p>
  </header>

  <section class="band about" id="about">
    <h2 class="band-title">ABOUT US</h2>
    <div class="band-body">
      <p>Lorem Ipsum is simply dummy text of the printing and typesetting industry. Lorem Ipsum has been the industry's standard dummy text ever since the 1500s, when an unknown printer took a galley of type and scrambled it to make a type specimen book. It has survived not only five centuries, but also the leap into electronic typesetting, remaining essentially unchanged. It was popularised in the 1960s with the release of Letraset sheets containing Lorem Ipsum passages, and more recently with desktop publishing software like Aldus PageMaker including versions of Lorem Ipsum.</p>
      <p>It is a long established fact that a reader will be distracted by the readable content of a page when looking at its layout. The point of using Lorem Ipsum is that it has a more-or-less normal distribution of letters, as opposed to using 'Content here, content here', making it look like readable English. Many desktop publishing packages and web page editors now use Lorem Ipsum as their default model text, and a search for 'lorem ipsum' will uncover many web sites still in their infancy. Various versions have evolved over the years, sometimes by accident, sometimes on purpose (injected humour and the like).</p>
    </div>
  </section>

  <section class="band train" id="train">
    <h2 class="band-title">TRAIN @ THE BRIMWELL PARLOUR</h2>
    <div class="band-body">
      <p>Lorem Ipsum is simply dummy text of the printing and typesetting industry. Lorem Ipsum has been the industry's standard dummy text ever since the 1500s, when an unknown printer took a galley of type and scrambled it to make a type specimen book. It has survived not only five centuries, but also the leap into electronic typesetting, remaining essentially unchanged.</p>
      <p>It was popularised in the 1960s with the release of Letraset sheets containing Lorem Ipsum passages, and more recently with desktop publishing software like Aldus PageMaker including versions of Lorem Ipsum.It is a long established fact that a reader will be distracted by the readable content of a page when looking at its layout.</p>
      <div class="train-visual" role="img" aria-label="White webcam illustration"></div>
    </div>
  </section>

  <section class="band remote" id="remote">
    <h2 class="band-title">WORK FROM HOME</h2>
    <div class="band-body">
      <p>Working as a webcam entertainer can be a very lucrative business, whether it is your only job or something you do on the side. It gives you the flexibility to create your own schedule based around your availability.</p>
      <div class="faq-links">
        <a class="faq-bubble" href="#need">What do<br>I need?</a>
        <a class="faq-bubble" href="#signup">How do<br>I sign up?</a>
      </div>
    </div>
  </section>

  <section class="band contact" id="contact">
    <h2 class="band-title">CONTACT US</h2>
    <div class="band-body">
      <svg class="contact-icon" width="146" height="146" viewBox="0 0 146 146" aria-hidden="true">
        <g fill="none" stroke="#fff" stroke-width="9" stroke-linejoin="miter">
          <rect x="28" y="38" width="90" height="70" transform="rotate(-45 73 73)"/>
          <polyline points="38,81 88,41 96,93" />
        </g>
      </svg>
      <form class="contact-form">
        <label for="f-name">Name</label>
        <input id="f-name" type="text">
        <label for="f-email">Email</label>
        <input id="f-email" type="email">
        <label for="f-comments">Comments</label>
        <textarea id="f-comments"></textarea>
      </form>
    </div>
  </section>
</body>
</html>
```